Powerpoint template for Kestrel Pathway Advisors

I would like to use my logo and colors to create a powerpoint deck that I can use for various presentations. I would want the design to be modern, use my logo on each page (small at the bottom by the slide number) and have a couple of transition slides for cover page, transition page, etc.

```html
<!DOCTYPE html>
<html lang="en">
<head>
<meta charset="utf-8">
<title>Kestrel Pathway Advisors – Presentation Template</title>
<link href="https://fonts.googleapis.com/css2?family=Montserrat:wght@400;500;600;700;800;900&display=swap" rel="stylesheet">
<style>
:root{
  --page:#8b8b8b;
  --blue:#2445e0;
  --blue-bright:#2f8ce6;
  --blue-deep:#1c33b8;
  --ink:#2b2b2b;
  --text:#3c3c3c;
  --grey:#4a4a4a;
  --white:#ffffff;
}
*{box-sizing:border-box;margin:0;padding:0}
html,body{width:1065px;height:1200px;overflow:hidden}
body{background:radial-gradient(ellipse at 50% 40%,#9a9a9a,var(--page));font-family:'Montserrat',sans-serif;color:var(--ink);position:relative}
.slide{position:absolute;width:454px;height:255px;overflow:hidden;background:var(--white);box-shadow:0 6px 14px rgba(0,0,0,.35)}
.col-l{left:72px}.col-r{left:539px}
.row-1{top:72px}.row-2{top:339px}.row-3{top:606px}.row-4{top:873px}
.abs{position:absolute}
.heading{position:absolute;left:24px;top:20px;font-size:14.5px;font-weight:400;letter-spacing:.2px;color:var(--ink);white-space:nowrap}
.heading b{font-weight:800;color:var(--blue)}
.body-copy{font-size:6.6px;line-height:12.75px;color:var(--text);text-align:justify}
.brand{font-weight:600;color:var(--blue);line-height:1.1;letter-spacing:.2px;white-space:nowrap}
.brand-foot{position:absolute;left:21px;top:224px;font-size:6.5px}
.footer{position:absolute;left:138px;top:223px;width:316px;height:19px;background:var(--blue);border-radius:10px 0 0 10px;color:var(--white);font-size:6.3px}
.footer svg{fill:var(--white)}
.footer .mail-ic{position:absolute;left:18px;top:6px;width:7px;height:7px}
.footer .mail{position:absolute;left:31px;top:5.5px}
.footer .sep{position:absolute;left:162px;top:5.5px}
.footer .tel-ic{position:absolute;left:173px;top:6px;width:7px;height:7px}
.footer .tel{position:absolute;left:184px;top:5.5px}
.footer .social{position:absolute;left:246px;top:5px;width:9px;height:9px;border-radius:50%;background:var(--white)}
.footer .num{position:absolute;left:293px;top:4.5px;width:11px;height:10px;border-radius:50%;background:var(--white);color:var(--blue);font-size:4.6px;font-weight:700;text-align:center;line-height:10px}
.faint-peaks{position:absolute;left:0;right:0;bottom:0;height:110px;background:linear-gradient(180deg,rgba(255,255,255,0),rgba(214,219,228,.85))}
.cover-photo{position:absolute;inset:0;background:linear-gradient(180deg,#38588a 0%,#6a84ad 30%,#b99a86 52%,#d9a06f 58%,#5d6a86 68%,#2c3350 85%,#1e2236 100%)}
.cover-brand{position:absolute;left:0;right:0;top:58px;text-align:center;color:var(--white);font-weight:600;font-size:22px;line-height:1.05;letter-spacing:1px}
.cover-brand span{display:block;font-size:8px;letter-spacing:2px}
.cover-band{position:absolute;left:90px;top:115px;width:340px;height:43px;background:linear-gradient(90deg,rgba(36,69,224,0),var(--blue) 18%,var(--blue) 82%,rgba(36,69,224,.4));color:var(--white);font-weight:800;font-size:11.5px;line-height:17px;text-align:center;padding-top:4.5px;padding-right:50px}
.cover-date{position:absolute;left:0;right:0;top:230px;text-align:center;color:var(--white);font-size:7px;font-weight:500}
.rel-photo{position:absolute;left:150px;top:0;width:304px;height:255px;background:linear-gradient(90deg,rgba(255,255,255,1) 0%,rgba(214,224,236,.7) 30%,#b8c4d4 55%,#5e6e8c 78%,#8fa2bf 100%)}
.toc-item{position:absolute;left:24px;font-size:7.5px;color:var(--ink);display:flex;align-items:center;gap:6px}
.toc-item i{font-style:normal;width:10.5px;height:10.5px;border-radius:50%;background:var(--blue);color:var(--white);font-size:4.6px;font-weight:700;display:flex;align-items:center;justify-content:center}
.svc-intro{position:absolute;left:167px;top:21px;width:268px;font-size:6.6px;line-height:12.75px;color:var(--text);text-align:justify}
.svc-note{position:absolute;font-size:5.8px;line-height:7.7px;color:var(--ink);width:100px}
.svc-note.left{text-align:right}
.about-photo{position:absolute;left:240px;top:125px;width:214px;height:96px;background:linear-gradient(180deg,rgba(255,255,255,0) 0%,rgba(60,80,200,.35) 30%,#2a3ab8 60%,#1b1d2a 100%)}
.check{position:absolute;left:24px;width:19px;height:19px;border-radius:50%;background:var(--blue)}
.check.dark{background:var(--grey)}
.check svg{position:absolute;left:5px;top:5px;width:9px;height:9px}
.graph-note{position:absolute;left:52px;width:148px;font-size:6.6px;line-height:11.5px;color:var(--text);text-align:justify}
.divider-photo{position:absolute;inset:0;background:linear-gradient(180deg,#2b4ee0 0%,#4f6fe6 35%,#8fa3d9 62%,#c7ccd8 80%,#8e95a8 100%)}
.center-brand{position:absolute;left:0;right:0;text-align:center;color:var(--white);font-weight:600;letter-spacing:1px;line-height:1.05}
.big-title{position:absolute;left:0;right:0;text-align:center;font-weight:900;font-size:27px;color:var(--white);letter-spacing:.3px}
.big-title b{color:var(--blue);font-weight:900}
.thanks-photo{position:absolute;inset:0;background:radial-gradient(circle at 84% 18%,#ffffff 0%,#dfe6ff 6%,rgba(120,150,255,.6) 18%,rgba(60,90,220,0) 40%),linear-gradient(180deg,#5d79ea 0%,#3c58d8 40%,#1c2b78 70%,#070a1c 100%)}
.thanks-contact{position:absolute;left:213px;top:202px;color:var(--white);font-size:6.5px;display:flex;align-items:center;gap:5px;white-space:nowrap}
.thanks-contact svg{width:7px;height:7px;fill:var(--white)}
.thanks-social{position:absolute;left:313px;top:224px;width:11px;height:11px;border-radius:50%;background:var(--white)}
</style>
</head>
<body>
<svg width="0" height="0" style="position:absolute">
  <defs>
    <symbol id="i-mail" viewBox="0 0 10 10"><path d="M0 2h10v6H0z" fill="currentColor"/><path d="M0.5 2.5L5 5.6 9.5 2.5" stroke="#2445e0" stroke-width=".8" fill="none"/></symbol>
    <symbol id="i-tel" viewBox="0 0 10 10"><path d="M2 0.5l2 2.2-1 1.3c.6 1.3 1.6 2.3 2.9 2.9l1.3-1 2.2 2-1.3 1.6C5 9.3.7 5 .4 1.8z"/></symbol>
  </defs>
</svg>

<!-- Cover -->
<section class="slide col-l row-1">
  <div class="cover-photo" role="img" aria-label="Photo of a mountain range at sunrise under a blue sky"></div>
  <div class="cover-brand">KESTREL<span>PATHWAY ADVISORS</span></div>
  <div class="cover-band">ELEVATE YOUR BUSINESS WITH<br>EXPERT CONSULTING</div>
  <div class="cover-date">January 24,2026</div>
</section>

<!-- Relationship management -->
<section class="slide col-r row-1">
  <div class="rel-photo" role="img" aria-label="Photo of a businessman walking up a giant upward-curving arrow into the clouds"></div>
  <h2 class="heading" style="line-height:20px"><b>RELATIONSHIP</b><br>MANAGEMENT</h2>
  <p class="body-copy abs" style="left:24px;top:66px;width:183px">Organizations that excel at account management achieve 15-20% higher client retention rates and generate 25% more revenue per client than those with ad-hoc approaches. We offer a comprehensive engagement to evaluate, redesign, and implement a world-class Strategic Account Management Program that transforms client relationships from transactional interactions into strategic partnerships.</p>
  <div class="brand brand-foot">Kestrel<br>Pathway Advisors</div>
  <div class="footer"><svg class="mail-ic" style="color:#fff"><use href="#i-mail"/></svg><span class="mail">hello@kestrelpathwayadvisors.com</span><span class="sep">|</span><svg class="tel-ic"><use href="#i-tel"/></svg><span class="tel">(555) 014-2297</span><span class="social"></span><span class="num">05</span></div>
</section>

<!-- Table of contents -->
<section class="slide col-l row-2">
  <div class="faint-peaks" role="img" aria-label="Faint snowy mountain range"></div>
  <h2 class="heading"><b>TABLE OF</b> CONTENTS</h2>
  <div class="toc-item" style="top:54px"><i>01</i>Keynote Speaker</div>
  <div class="toc-item" style="top:81px"><i>02</i>Relationship Management</div>
  <div class="toc-item" style="top:108px"><i>03</i>Executive Leadership Coaching</div>
  <div class="toc-item" style="top:136px"><i>04</i>Growth Strategies</div>
  <div class="toc-item" style="top:163px"><i>05</i>About us</div>
  <svg class="abs" style="left:0;top:0" width="454" height="255" viewBox="0 0 454 255">
    <defs><linearGradient id="tocPhoto" x1="0" y1="0" x2="1" y2="1"><stop offset="0" stop-color="#dfe2ea"/><stop offset=".5" stop-color="#9a9ca3"/><stop offset="1" stop-color="#b8865a"/></linearGradient></defs>
    <path role="img" aria-label="Photo of two businesswomen reviewing a tablet together" d="M219 50L327 12 437 50V210Q330 193 219 206Z" fill="url(#tocPhoto)"/>
    <path d="M219 207Q330 195 437 210 437 216 434 216Q330 202 219 214Z" fill="#2445e0"/>
  </svg>
  <div class="brand brand-foot">Kestrel<br>Pathway Advisors</div>
  <div class="footer"><svg class="mail-ic" style="color:#fff"><use href="#i-mail"/></svg><span class="mail">hello@kestrelpathwayadvisors.com</span><span class="sep">|</span><svg class="tel-ic"><use href="#i-tel"/></svg><span class="tel">(555) 014-2297</span><span class="social"></span><span class="num">02</span></div>
</section>

<!-- Our services -->
<section class="slide col-r row-2">
  <h2 class="heading"><b>OUR</b> SERVICES</h2>
  <p class="svc-intro">Sed ut perspiciatis unde omnis iste natus error sit voluptatem accusantium doloremquriauae ab illo inventore veritatis et ecto beatae vitae dicta suo.</p>
  <svg class="abs" style="left:0;top:0" width="454" height="255" viewBox="0 0 454 255">
    <defs><filter id="soft" x="-30%" y="-30%" width="160%" height="160%"><feDropShadow dx="0" dy="1" stdDeviation="3" flood-opacity=".25"/></filter></defs>
    <path d="M217.4,94.0 L210.4,60.8 A80,80 0 0 0 156.4,101.4 L186.4,117.4 A46,46 0 0 1 217.4,94.0Z" fill="#8f8f8f"/>
    <path d="M185.7,118.8 L149.7,101.3 A86,86 0 0 0 149.7,176.7 L185.7,159.2 A46,46 0 0 1 185.7,118.8Z" fill="#a2a2a2"/>
    <path d="M186.4,160.6 L156.4,176.6 A80,80 0 0 0 210.4,217.2 L217.4,184.0 A46,46 0 0 1 186.4,160.6Z" fill="#7d7d7d"/>
    <path d="M236.6,94.0 L243.6,60.8 A80,80 0 0 1 297.6,101.4 L267.6,117.4 A46,46 0 0 0 236.6,94.0Z" fill="#2a55db"/>
    <path d="M268.3,118.8 L304.3,101.3 A86,86 0 0 1 304.3,176.7 L268.3,159.2 A46,46 0 0 0 268.3,118.8Z" fill="#2f8ce6"/>
    <path d="M267.6,160.6 L297.6,176.6 A80,80 0 0 1 243.6,217.2 L236.6,184.0 A46,46 0 0 0 267.6,160.6Z" fill="#2c4cb8"/>
    <g fill="none" stroke="#fff" stroke-width="1">
      <rect x="174" y="97" width="11" height="11"/><circle cx="164" cy="139" r="6"/><path d="M174 172l6 6 4-8 4 6"/>
      <rect x="275" y="97" width="11" height="11"/><circle cx="290" cy="139" r="6"/><circle cx="290" cy="139" r="3"/><path d="M272 176l6-6 3 6 5-4"/>
    </g>
    <circle cx="227" cy="139" r="44" fill="#fff" filter="url(#soft)"/>
    <g stroke="#2a3a8a" stroke-width=".6" fill="#2a3a8a">
      <line x1="135" y1="82" x2="158" y2="82"/><circle cx="158" cy="82" r="1.3"/>
      <line x1="116" y1="137" x2="136" y2="137"/><circle cx="136" cy="137" r="1.3"/>
      <line x1="140" y1="192" x2="158" y2="192"/><circle cx="158" cy="192" r="1.3"/>
      <line x1="296" y1="82" x2="316" y2="82"/><circle cx="296" cy="82" r="1.3"/>
      <line x1="319" y1="137" x2="340" y2="137"/><circle cx="319" cy="137" r="1.3"/>
      <line x1="296" y1="192" x2="316" y2="192"/><circle cx="296" cy="192" r="1.3"/>
    </g>
  </svg>
  <div class="brand abs" style="left:185px;top:131px;width:84px;text-align:center;font-size:7.5px">Kestrel<br>Pathway Advisors</div>
  <p class="svc-note left" style="left:29px;top:76px">Sed ut perspiciatis unde omnis iste natus error sit voluptatem accusant inre veritatis et ecto beatae vitae dicta suo.</p>
  <p class="svc-note left" style="left:9px;top:130px">Sed ut perspiciatis unde omnis iste natus error sit voluptatem accusant inre veritatis</p>
  <p class="svc-note left" style="left:32px;top:183px">Sed ut perspiciatis unde omnis iste natus error sit voluptatem accusant inre veritatis et ecto beatae vitae dicta suo.</p>
  <p class="svc-note" style="left:325px;top:76px">Sed ut perspiciatis unde omnis iste natus error sit voluptatem accusant inre veritatis et ecto beatae vitae dicta suo.</p>
  <p class="svc-note" style="left:345px;top:130px">Sed ut perspiciatis unde omnis iste natus error sit voluptatem accusant inre veritatis</p>
  <p class="svc-note" style="left:325px;top:183px">Sed ut perspiciatis unde omnis iste natus error sit voluptatem accusant inre veritatis et ecto beatae vitae dicta suo.</p>
  <div class="brand brand-foot">Kestrel<br>Pathway Advisors</div>
  <div class="footer"><svg class="mail-ic" style="color:#fff"><use href="#i-mail"/></svg><span class="mail">hello@kestrelpathwayadvisors.com</span><span class="sep">|</span><svg class="tel-ic"><use href="#i-tel"/></svg><span class="tel">(555) 014-2297</span><span class="social"></span><span class="num">06</span></div>
</section>

<!-- About us -->
<section class="slide col-l row-3">
  <div class="faint-peaks" role="img" aria-label="Faint snowy mountain range"></div>
  <h2 class="heading"><b>ABOUT</b> US</h2>
  <p class="body-copy abs" style="left:24px;top:44px;width:183px">Kestrel Pathway Advisors was created in 2025 by Dana Merrow. Dana has over 30 years in the Fleet Management Industry and climbed the ranks from Executive Assistant to the Chief Client Officer of a $10 billion enterprise. Dana brings her years of experience in Strategic Account Management, client retention &amp; satisfaction, mentorship, leadership, culture, along with her own experiences working with family-owned to Private Equity-owned structures, to inspire and grow our next generation of leaders.</p>
  <p class="body-copy abs" style="left:237px;top:44px;width:178px">Our mission is to empower leaders and companies to design intentional, results-driven leaders and processes. Through strategic guidance and a focus on authenticity and integrity, we help individuals unlock their potential, lead with courage, achieve results, and create a legacy of impact and purpose.</p>
  <div class="about-photo" role="img" aria-label="Illustration of mountain peaks with a rising arrow, framing a portrait of the founder"></div>
  <div class="brand brand-foot">Kestrel<br>Pathway Advisors</div>
  <div class="footer"><svg class="mail-ic" style="color:#fff"><use href="#i-mail"/></svg><span class="mail">hello@kestrelpathwayadvisors.com</span><span class="sep">|</span><svg class="tel-ic"><use href="#i-tel"/></svg><span class="tel">(555) 014-2297</span><span class="social"></span><span class="num">03</span></div>
</section>

<!-- Our graph -->
<section class="slide col-r row-3">
  <h2 class="heading"><b>OUR</b> GRAPH</h2>
  <div class="check" style="top:63px"><svg viewBox="0 0 10 10"><path d="M1.5 5.2l2.3 2.3L8.5 2.5" stroke="#fff" stroke-width="1.4" fill="none"/></svg></div>
  <div class="check dark" style="top:109px"><svg viewBox="0 0 10 10"><path d="M1.5 5.2l2.3 2.3L8.5 2.5" stroke="#fff" stroke-width="1.4" fill="none"/></svg></div>
  <div class="check" style="top:155px"><svg viewBox="0 0 10 10"><path d="M1.5 5.2l2.3 2.3L8.5 2.5" stroke="#fff" stroke-width="1.4" fill="none"/></svg></div>
  <p class="graph-note" style="top:61px">Sed ut perspiciatis unde omnis iste natus errorvoluptatusantoloremb illo inventore verito beatae vitae dicta suo.</p>
  <p class="graph-note" style="top:107px">Sed ut perspiciatis unde omnis iste natus errorvoluptatusantoloremb illo inventore verito beatae vitae dicta suo.</p>
  <p class="graph-note" style="top:153px">Sed ut perspiciatis unde omnis iste natus errorvoluptatusantoloremb illo inventore verito beatae vitae dicta suo.</p>
  <svg class="abs" style="left:0;top:0" width="454" height="255" viewBox="0 0 454 255" font-family="Montserrat, sans-serif">
    <g font-size="4.6" fill="#333" text-anchor="end">
      <text x="236" y="200">0</text><text x="236" y="184">1</text><text x="236" y="168">2</text><text x="236" y="153">3</text><text x="236" y="137">4</text><text x="236" y="121">5</text><text x="236" y="105">6</text><text x="236" y="89">7</text><text x="236" y="73">8</text><text x="236" y="57">9</text><text x="236" y="41">10</text>
    </g>
    <line x1="246.5" y1="35" x2="246.5" y2="198" stroke="#444" stroke-width=".6"/>
    <line x1="246.5" y1="198" x2="435" y2="198" stroke="#444" stroke-width=".6"/>
    <rect x="259.5" y="126.4" width="13" height="71.6" fill="#4a4a4a"/>
    <rect x="289.5" y="118.5" width="13" height="79.5" fill="#2445e0"/>
    <rect x="320.5" y="85.1" width="13" height="112.9" fill="#4a4a4a"/>
    <rect x="350.5" y="118.5" width="13" height="79.5" fill="#2445e0"/>
    <rect x="380.5" y="126.4" width="13" height="71.6" fill="#4a4a4a"/>
    <rect x="411.5" y="85.1" width="13" height="112.9" fill="#2445e0"/>
    <g font-size="4.6" fill="#333" text-anchor="middle">
      <text x="266" y="122">4.5%</text><text x="296" y="114">5%</text><text x="327" y="81">7.1%</text><text x="357" y="114">5%</text><text x="387" y="122">4.5%</text><text x="418" y="81">7.1%</text>
      <text x="266" y="205">2000</text><text x="296" y="205">2005</text><text x="327" y="205">2010</text><text x="357" y="205">2015</text><text x="387" y="205">2020</text><text x="418" y="205">2024</text>
    </g>
  </svg>
  <div class="brand brand-foot">Kestrel<br>Pathway Advisors</div>
  <div class="footer"><svg class="mail-ic" style="color:#fff"><use href="#i-mail"/></svg><span class="mail">hello@kestrelpathwayadvisors.com</span><span class="sep">|</span><svg class="tel-ic"><use href="#i-tel"/></svg><span class="tel">(555) 014-2297</span><span class="social"></span><span class="num">07</span></div>
</section>

<!-- Section divider -->
<section class="slide col-l row-4">
  <div class="divider-photo" role="img" aria-label="Photo of snow-capped mountains under a blue cloudy sky"></div>
  <div class="center-brand" style="top:64px;font-size:17px">KESTREL<br><span style="font-size:6.5px;letter-spacing:2px">PATHWAY ADVISORS</span></div>
  <div class="big-title" style="top:110px">SECTION <b>DIVIDER</b></div>
</section>

<!-- Thank you -->
<section class="slide col-r row-4">
  <div class="thanks-photo" role="img" aria-label="Photo of a dark mountain silhouette against a blue sky with the sun bursting over the ridge and a rising arrow graphic"></div>
  <div class="abs" style="left:42px;top:58px;color:#fff;font-weight:600;font-size:19px;letter-spacing:1px;line-height:1.05">KESTREL<br><span style="font-size:6.5px;letter-spacing:2px">PATHWAY ADVISORS</span></div>
  <div class="big-title" style="left:233px;right:auto;top:155px;font-size:26px">THANK <b>YOU</b></div>
  <div class="thanks-contact"><svg style="color:#fff"><use href="#i-mail"/></svg><span>hello@kestrelpathwayadvisors.com</span><span>&nbsp;|&nbsp;</span><svg><use href="#i-tel"/></svg><span>(555) 014-2297</span></div>
  <div class="thanks-social"></div>
</section>
</body>
</html>
```